Business Card Design for a Sound engineer and DJ

We would like a residn of the business card.

Logo must remain the same.
The card is for the owner of the company.
The business card is in Arabic as the company is based in Kuwait.
The company specializes in sound engineering for singers concerts and events and in addition DJ.
The color options is up to the designer but we would like it masculine as the owner is a man.

Target Market(s)

All ages

Industry/Entity Type

Media

Contact Information for Business Card

Name:
Eng. Tarek Halabi
م/طارق حلبي

The name above is in Arabic and English.

Title: General Manager
Mobile: +965 66307852
Office: +965 22486037
Email: info@sawtarin.net

Address:
Office no. 3
1st floor
Almarfa Complex
Rashed AlQeblawi St.
Salmiya
Kuwait

Instagram: @sawtarin
Snap: sawtarin

Requirements
Nice to have
• can we have Instagram icon and snap icon and a phone vector and email?
• Instead of writing the words

```html
<!DOCTYPE html>
<html lang="en">
<head>
<meta charset="utf-8">
<title>Sawtarin Business Card</title>
<link href="https://fonts.googleapis.com/css2?family=Open+Sans:wght@400;600&family=Cairo:wght@400;600&display=swap" rel="stylesheet">
<style>
  :root {
    --page-bg: #d9d6d3;
    --card-black: #141414;
    --ink-white: #f1f1f1;
    --ink-grey: #a3a3a3;
    --accent-magenta: #c22cb0;
    --accent-blue: #8f93e8;
    --divider: #4a4a4a;
  }
  * { margin: 0; padding: 0; box-sizing: border-box; }
  html, body { width: 1200px; height: 814px; overflow: hidden; }
  body {
    background: var(--page-bg);
    font-family: "Open Sans", Arial, sans-serif;
    position: relative;
  }
  .card {
    position: absolute;
    top: 252px;
    width: 540px;
    height: 309px;
    background: var(--card-black);
    border-radius: 4px;
    box-shadow: 0 6px 18px rgba(0,0,0,0.25);
    overflow: hidden;
  }

  /* Back side */
  .card-back { left: 30px; }
  .social-list {
    position: absolute; top: 24px; right: 24px;
    display: flex; align-items: center; gap: 14px;
    list-style: none;
    color: var(--ink-white); font-size: 12px; font-weight: 400;
  }
  .social-list li { display: flex; align-items: center; gap: 6px; }
  .social-mark {
    width: 16px; height: 16px; background: var(--ink-white); border-radius: 3px;
  }
  .card-back .brand-lockup {
    position: absolute; top: 104px; left: 0; right: 0;
    display: flex; flex-direction: column; align-items: center;
    color: var(--ink-grey);
  }
  .brand-name { display: flex; align-items: center; gap: 10px; font-size: 30px; font-weight: 600; }
  .brand-square { width: 18px; height: 18px; background: currentColor; }
  .brand-tagline { margin-top: 8px; font-size: 12px; font-weight: 400; }
  .brand-tagline-ar { margin-top: 2px; font-family: "Cairo", Arial, sans-serif; font-size: 13px; font-weight: 400; }
  .card-back .website {
    position: absolute; top: 232px; left: 0; right: 0;
    text-align: center; color: var(--ink-white);
    font-size: 14px; letter-spacing: 3px;
  }

  /* Front side */
  .card-front { left: 630px; }
  .card-front .brand-lockup {
    position: absolute; left: 0; top: 0; width: 250px; height: 100%;
    display: flex; flex-direction: column; align-items: center; justify-content: center;
    color: var(--accent-magenta);
  }
  .card-front .brand-lockup .brand-tagline,
  .card-front .brand-lockup .brand-tagline-ar { color: var(--accent-blue); }
  .divider {
    position: absolute; left: 250px; top: 30px; bottom: 30px;
    width: 1px; background: var(--divider);
  }
  .contact-block {
    position: absolute; left: 272px; top: 44px; right: 16px;
    color: var(--ink-white);
  }
  .person-name { color: var(--accent-magenta); font-size: 21px; font-weight: 600; line-height: 1.15; }
  .person-name-ar {
    color: var(--accent-magenta); font-family: "Cairo", Arial, sans-serif;
    font-size: 17px; font-weight: 600; line-height: 1.3; text-align: left;
  }
  .person-title { color: var(--accent-blue); font-size: 15px; margin-top: 2px; }
  .address { margin-top: 12px; font-size: 14px; line-height: 1.4; }
  .contact-list { margin-top: 8px; list-style: none; font-size: 14px; line-height: 1.6; }
  .contact-list li { display: flex; align-items: center; gap: 8px; }
  .contact-list svg { width: 14px; height: 14px; fill: var(--accent-magenta); flex: none; }
</style>
</head>
<body>
  <section class="card card-back">
    <ul class="social-list">
      <li><span class="social-mark"></span>sawtarin</li>
      <li><span class="social-mark"></span>@sawtarin</li>
    </ul>
    <div class="brand-lockup">
      <div class="brand-name"><span class="brand-square"></span>SAWTARIN</div>
      <div class="brand-tagline">DJ - SOUND ENG. - LIGHTING</div>
      <div class="brand-tagline-ar" dir="rtl">دي جي - هندسة صوت - إضاءة</div>
    </div>
    <div class="website">www.sawtarin.net</div>
  </section>

  <section class="card card-front">
    <div class="brand-lockup">
      <div class="brand-name"><span class="brand-square"></span>SAWTARIN</div>
      <div class="brand-tagline">DJ - SOUND ENG. - LIGHTING</div>
      <div class="brand-tagline-ar" dir="rtl">دي جي - هندسة صوت - إضاءة</div>
    </div>
    <div class="divider"></div>
    <div class="contact-block">
      <div class="person-name">Tarek Halabi</div>
      <div class="person-name-ar" dir="rtl">م/طارق حلبي</div>
      <div class="person-title">General Manager</div>
      <div class="address">Office no. 3, 1st floor<br>Almarfa Complex<br>Rashed AlQeblawi St.<br>Salmiya, Kuwait</div>
      <ul class="contact-list">
        <li><svg viewBox="0 0 14 14"><rect x="3" y="0" width="8" height="14" rx="1.5"/><rect x="4.5" y="2" width="5" height="8" fill="#141414"/></svg>+965 66307852</li>
        <li><svg viewBox="0 0 14 14"><path d="M3 1l2.5 0 1 3.5-1.6 1.2a8 8 0 0 0 3.4 3.4l1.2-1.6 3.5 1v2.5c0 .8-.7 1-1.5 1C5.8 12 2 8.2 2 2.5 2 1.7 2.2 1 3 1z"/></svg>+965 22486037</li>
        <li><svg viewBox="0 0 14 14"><rect x="0" y="2" width="14" height="10" rx="1"/><path d="M1 3l6 5 6-5" stroke="#141414" stroke-width="1.2" fill="none"/></svg>info@sawtarin.net</li>
      </ul>
    </div>
  </section>
</body>
</html>
```